Beauty Salon Design

The business card design will be for a new beauty salon opening up.

The therapist has over 11 years at a leading beauty Salon in perth.

The two colours that the salon will use is black and gold.

Industry/Entity Type

Beauty Salon

Contact Information for Business Card

Lumora Beauty

Corinne Halstead Pryce
Advanced beauty therapist
0455 817 302

Monday - Friday 9am - 2.30pm
Weekends and nights by appointment only

Waxing, Tinting, Swedish massage, hot stone massage, facials, peels, micro, LED light treatment, skin needling and retail products.

```html
<!DOCTYPE html>
<html lang="en">
<head>
<meta charset="utf-8">
<title>Lumora Beauty – Business Card Back</title>
<link rel="stylesheet" href="https://fonts.googleapis.com/css2?family=Alegreya:ital,wght@1,400&display=swap">
<style>
  :root {
    --card-black: #000000;
    --gold: #c9b27a;
    --gold-deep: #6f6242;
    --gold-shadow: #2a251a;
  }
  html, body {
    margin: 0;
    padding: 0;
    width: 1200px;
    height: 741px;
    overflow: hidden;
    background: var(--card-black);
  }
  .card {
    position: relative;
    width: 1200px;
    height: 741px;
    background: var(--card-black);
    color: var(--gold);
    font-family: "Alegreya", Georgia, serif;
    font-style: italic;
    font-weight: 400;
  }
  .corner-ornament {
    position: absolute;
    display: block;
  }
  .corner-ornament--top-left { left: 54px; top: 41px; width: 214px; height: 285px; }
  .corner-ornament--top-right { left: 940px; top: 41px; width: 217px; height: 289px; }
  .corner-ornament--bottom-left { left: 48px; top: 486px; width: 287px; height: 217px; }
  .corner-ornament--bottom-right { left: 940px; top: 411px; width: 217px; height: 292px; }

  .services,
  .contact {
    position: absolute;
    left: 0;
    right: 0;
    margin: 0;
    text-align: center;
    font-size: 43px;
    line-height: 54px;
    white-space: nowrap;
  }
  .services { top: 130px; }
  .contact { top: 449px; }
  .services span,
  .contact span { display: block; }
</style>
</head>
<body>
  <main class="card">
    <svg class="corner-ornament corner-ornament--top-left" viewBox="0 0 214 285" role="img" aria-label="Gold filigree scroll corner ornament">
      <defs>
        <radialGradient id="ornTL" cx="0" cy="0" r="1.1">
          <stop offset="0" stop-color="#6f6242"/>
          <stop offset="1" stop-color="#2a251a" stop-opacity="0.15"/>
        </radialGradient>
      </defs>
      <path d="M0 0 H214 V40 L150 70 L100 130 L70 210 L60 285 H0 Z" fill="url(#ornTL)"/>
    </svg>
    <svg class="corner-ornament corner-ornament--top-right" viewBox="0 0 217 289" role="img" aria-label="Gold filigree scroll corner ornament">
      <defs>
        <radialGradient id="ornTR" cx="1" cy="0" r="1.1">
          <stop offset="0" stop-color="#6f6242"/>
          <stop offset="1" stop-color="#2a251a" stop-opacity="0.15"/>
        </radialGradient>
      </defs>
      <path d="M217 0 H0 V40 L64 70 L114 130 L144 210 L154 289 H217 Z" fill="url(#ornTR)"/>
    </svg>
    <svg class="corner-ornament corner-ornament--bottom-left" viewBox="0 0 287 217" role="img" aria-label="Gold filigree scroll corner ornament">
      <defs>
        <radialGradient id="ornBL" cx="0" cy="1" r="1.1">
          <stop offset="0" stop-color="#6f6242"/>
          <stop offset="1" stop-color="#2a251a" stop-opacity="0.15"/>
        </radialGradient>
      </defs>
      <path d="M0 217 H287 V150 L230 140 L150 110 L90 60 L70 0 H0 Z" fill="url(#ornBL)"/>
    </svg>
    <svg class="corner-ornament corner-ornament--bottom-right" viewBox="0 0 217 292" role="img" aria-label="Gold filigree scroll corner ornament">
      <defs>
        <radialGradient id="ornBR" cx="1" cy="1" r="1.1">
          <stop offset="0" stop-color="#6f6242"/>
          <stop offset="1" stop-color="#2a251a" stop-opacity="0.15"/>
        </radialGradient>
      </defs>
      <path d="M217 292 H0 V230 L60 210 L110 150 L145 70 L155 0 H217 Z" fill="url(#ornBR)"/>
    </svg>

    <p class="services">
      <span>Waxing, Tinting, Swedish massage,</span>
      <span>hot stone massage, facials, peels,</span>
      <span>micro, LED light treatment, skin</span>
      <span>needling and retail products.</span>
    </p>

    <p class="contact">
      <span class="contact__phone">0455 817 302</span>
      <span class="contact__hours">Monday - Friday 9am - 2.30pm</span>
      <span class="contact__note">Weekends and nights by appointment only</span>
    </p>
  </main>
</body>
</html>
```